Brisk Thread Custom Apparel Flyer

We're a custom clothing manufacturer marketing to the cycling, triathlon, running and fitness community.
- v
- We offer quick turnaround on custom, small quantity orders
- Our clothing is American Made
- We offer top quality materials and workmanship
- Pricing is extremely competitive
- We market to small businesses, casual athletes, clubs, charitable organizations and race teams
- Athlete owned and operated
-These flyers will be displayed in Bicycle and Running Retail stores, and at events
Photos and information is available at artist's request

Target Market(s)

We offer custom design services for casual clothing(hats, tshirts, jackets) and custom printed apparel for these sports as well.

These flyers will be displayed in Bicycle and Running Retail stores, and at events

Industry/Entity Type

Clothing

Font styles to use
Sans Serif
Other font styles liked:
• Sporty and easy to read

Requirements
Must have
• Please use this link as a guideline to show the design process
• http://portal.velomarkit.net/Login/en-US/
• pedalbrisk@mailory.net
• (555)317-6290
• Made in the USA
• NO Minimums
• Youth sizes
• Women's sizes
• Up to 4XL in Race and Club fit
• Custom Cycling, Triathlon, Running, Fitness and Casual Apparel
• Our company color is 801c
Nice to have
• Cant think of right now
Should not have
• Adult content

```html
<!DOCTYPE html>
<html lang="en">
<head>
<meta charset="utf-8">
<title>Brisk Thread Custom Apparel Flyer</title>
<link rel="stylesheet" href="https://fonts.googleapis.com/css2?family=Archivo+Black&family=Oswald:wght@700&family=Roboto:ital,wght@0,400;0,700;1,900&display=swap">
<style>
  :root {
    --backdrop: #4a4a4d;
    --paper: #ffffff;
    --brand-deep: #0b5a86;
    --brand-mid: #0a7fb5;
    --brand-bright: #07a3da;
    --ink-navy: #0c5580;
  }
  html, body {
    margin: 0;
    width: 1200px;
    height: 1200px;
    overflow: hidden;
    background: var(--backdrop);
  }
  .flyer {
    position: absolute;
    left: 240px;
    top: 91px;
    width: 720px;
    height: 1018px;
    display: block;
  }
  .perk { font-family: "Roboto", sans-serif; font-weight: 900; font-style: italic; font-size: 29px; fill: var(--ink-navy); }
  .headline { font-family: "Archivo Black", sans-serif; font-size: 170px; fill: var(--paper); }
  .subhead { font-family: "Oswald", sans-serif; font-weight: 700; font-size: 70px; fill: var(--paper); }
  .mission { font-family: "Oswald", sans-serif; font-weight: 700; font-size: 23px; fill: var(--paper); letter-spacing: 0.3px; }
  .benefit { font-family: "Roboto", sans-serif; font-weight: 400; font-size: 22.5px; fill: var(--paper); }
  .contact-phone { font-family: "Roboto", sans-serif; font-weight: 700; font-size: 33px; fill: var(--ink-navy); }
  .contact-mail { font-family: "Roboto", sans-serif; font-weight: 700; font-size: 28px; fill: var(--ink-navy); }
</style>
</head>
<body>
<svg class="flyer" viewBox="0 0 900 1273" xmlns="http://www.w3.org/2000/svg">
  <defs>
    <linearGradient id="floor-fade" x1="0" y1="0" x2="0" y2="1">
      <stop offset="0" stop-color="#dcdfe2"/>
      <stop offset="1" stop-color="#ffffff"/>
    </linearGradient>
    <linearGradient id="athlete-tones" x1="0" y1="0" x2="0" y2="1">
      <stop offset="0" stop-color="#c9b8ae"/>
      <stop offset="0.25" stop-color="#b3242a"/>
      <stop offset="0.55" stop-color="#1d1f24"/>
      <stop offset="0.8" stop-color="#8a5c4c"/>
      <stop offset="1" stop-color="#d9dadc"/>
    </linearGradient>
    <symbol id="tick-circle" viewBox="0 0 28 28">
      <circle cx="13" cy="15" r="10.5" fill="none" stroke="currentColor" stroke-width="3"/>
      <path d="M7.5 14.5 L12.5 20 L25 3" fill="none" stroke="currentColor" stroke-width="3.6" stroke-linecap="round" stroke-linejoin="round"/>
    </symbol>
  </defs>

  <!-- paper and bands -->
  <rect class="paper" width="900" height="1273" fill="var(--paper)"/>
  <rect y="1040" width="900" height="233" fill="url(#floor-fade)"/>
  <polygon class="band-bright" points="0,723 899,640 899,1083 0,1138" fill="var(--brand-bright)"/>
  <polygon class="band-mid" points="0,723 899,640 899,665 0,753" fill="var(--brand-mid)"/>
  <polygon class="band-deep" points="0,231 899,143 899,655 0,723" fill="var(--brand-deep)"/>
  <polygon class="band-accent" points="533,180 899,110 899,143 508,181" fill="var(--brand-mid)"/>

  <!-- athlete photo area -->
  <polygon role="img" aria-label="Photo of a cyclist in a red and black custom kit and helmet standing beside a red road bike"
           points="700,250 899,250 899,1250 470,1250 470,660 600,560" fill="url(#athlete-tones)"/>

  <!-- top perks -->
  <g class="perks">
    <use href="#tick-circle" x="52" y="55" width="28" height="28" color="var(--ink-navy)"/>
    <text class="perk" x="86" y="80">NO MINIMUMS</text>
    <use href="#tick-circle" x="52" y="103" width="28" height="28" color="var(--ink-navy)"/>
    <text class="perk" x="86" y="128">YOUTH SIZES</text>
    <use href="#tick-circle" x="52" y="152" width="28" height="28" color="var(--ink-navy)"/>
    <text class="perk" x="86" y="177">WOMEN’S SIZES</text>
    <use href="#tick-circle" x="384" y="55" width="28" height="28" color="var(--ink-navy)"/>
    <text class="perk" x="418" y="80">UP TO 4XL IN RACE</text>
    <text class="perk" x="418" y="117">AND CLUB FIT</text>
  </g>

  <!-- headline block -->
  <g class="headline-block" transform="rotate(-4 48 500)">
    <text class="headline" x="48" y="393" textLength="652" lengthAdjust="spacingAndGlyphs">BRISK</text>
    <text class="headline" x="48" y="508" textLength="575" lengthAdjust="spacingAndGlyphs">THREAD</text>
    <text class="subhead" x="48" y="585" textLength="562" lengthAdjust="spacingAndGlyphs">CUSTOM APPAREL</text>
    <text class="mission" x="48" y="625">WE'RE A CUSTOM CLOTHING MANUFACTURER</text>
    <text class="mission" x="48" y="657">MARKETING TO THE CYCLING, TRIATHLON,</text>
    <text class="mission" x="48" y="689">RUNNING AND FITNESS COMMUNITY.</text>
  </g>

  <!-- benefits list -->
  <g class="benefits">
    <use href="#tick-circle" x="55" y="757" width="26" height="26" color="var(--paper)"/>
    <text class="benefit" x="90" y="777">We offer quick turnaround on</text>
    <text class="benefit" x="90" y="805">custom, small quantity orders</text>
    <use href="#tick-circle" x="55" y="823" width="26" height="26" color="var(--paper)"/>
    <text class="benefit" x="90" y="843">Our clothing is American Made</text>
    <use href="#tick-circle" x="55" y="861" width="26" height="26" color="var(--paper)"/>
    <text class="benefit" x="90" y="881">We offer top quality materials and</text>
    <text class="benefit" x="90" y="909">workmanship</text>
    <use href="#tick-circle" x="55" y="927" width="26" height="26" color="var(--paper)"/>
    <text class="benefit" x="90" y="947">is extremely competitive</text>
    <use href="#tick-circle" x="55" y="965" width="26" height="26" color="var(--paper)"/>
    <text class="benefit" x="90" y="985">We market to small businesses,</text>
    <text class="benefit" x="90" y="1013">casual athletes, clubs, charitable</text>
    <text class="benefit" x="90" y="1041">organizations and race teams</text>
    <use href="#tick-circle" x="55" y="1059" width="26" height="26" color="var(--paper)"/>
    <text class="benefit" x="88" y="1078">Athlete owned and operated</text>
  </g>

  <!-- contact -->
  <g class="contact">
    <circle cx="72" cy="1167" r="16" fill="none" stroke="var(--brand-bright)" stroke-width="2.5"/>
    <path d="M65 1158 q-2 4 3 11 q5 7 10 7 l3 -3 l-4 -4 l-3 2 q-4 -2 -6 -7 l2 -3 l-3 -5 z" fill="var(--brand-bright)"/>
    <text class="contact-phone" x="110" y="1179">(555)317-6290</text>
    <circle cx="72" cy="1211" r="16" fill="none" stroke="var(--brand-bright)" stroke-width="2.5"/>
    <rect x="63" y="1204" width="18" height="13" rx="1.5" fill="none" stroke="var(--brand-bright)" stroke-width="2"/>
    <path d="M63 1205 l9 7 l9 -7" fill="none" stroke="var(--brand-bright)" stroke-width="2"/>
    <text class="contact-mail" x="96" y="1220">pedalbrisk@mailory.net</text>
  </g>
</svg>
</body>
</html>
```